" A empresa atua em dois segmentos: 1) atendimento psicológico de crianças, adolescentes e adultos e 2) recrutamento, seleçao e treinamento de pessoas. A proposta é trabalhar com o desenvolvimento humano em suas diversas dimensoes. "

```html
<!DOCTYPE html>
<html lang="pt-BR">
<head>
<meta charset="utf-8">
<title>Trilha Viva – Envelopes</title>
<link href="https://fonts.googleapis.com/css2?family=Questrial&display=swap" rel="stylesheet">
<style>
  :root {
    --teal: #1aa6a6;
    --teal-light: #30bdbc;
    --flap-gray: #5e5f61;
    --paper: #ffffff;
    --ink-gray: #6a6b6d;
    --backdrop: #e9e7e3;
  }
  html, body {
    margin: 0;
    width: 1200px;
    height: 1200px;
    overflow: hidden;
    background: var(--backdrop);
    font-family: "Questrial", sans-serif;
  }
  .canvas { position: relative; width: 1200px; height: 1200px; }

  .envelope { position: absolute; left: 132px; width: 936px; }
  .envelope-front { top: 91px; height: 533px; }
  .envelope-back { top: 684px; height: 408px; }
  .envelope svg.shape { position: absolute; inset: 0; }

  .brand {
    position: absolute; left: 156px; top: 232px;
    display: flex; align-items: center;
  }
  .brand-dot {
    width: 48px; height: 48px; border-radius: 50%;
    background: var(--teal);
  }
  .brand-divider {
    width: 2px; height: 56px; background: var(--teal);
    margin: 0 8px 0 14px;
  }
  .brand-name {
    font-size: 34px; line-height: 1; color: var(--teal);
    letter-spacing: 0.5px;
  }
  .brand-tagline {
    font-size: 15px; color: var(--ink-gray); margin-top: 4px;
    letter-spacing: 0.6px;
  }

  .contact {
    position: absolute; left: 161px; top: 983px;
    color: var(--paper); font-size: 14px; line-height: 17px;
    letter-spacing: 0.3px;
  }
</style>
</head>
<body>
<div class="canvas">

  <section class="envelope envelope-front">
    <svg class="shape" width="936" height="533" viewBox="0 0 936 533">
      <rect x="0" y="113" width="936" height="420" fill="var(--paper)"/>
      <polygon points="96,0 840,0 936,113 0,113" fill="var(--flap-gray)"/>
    </svg>
  </section>

  <div class="brand">
    <div class="brand-dot"></div>
    <div class="brand-divider"></div>
    <div>
      <div class="brand-name">Trilha Viva</div>
      <div class="brand-tagline">Desenvolvimento Humano</div>
    </div>
  </div>

  <section class="envelope envelope-back">
    <svg class="shape" width="936" height="408" viewBox="0 0 936 408">
      <rect x="0" y="0" width="936" height="408" fill="var(--teal)"/>
      <polygon points="7,0 929,0 830,115 106,115" fill="var(--flap-gray)"/>
      <circle cx="816" cy="216" r="132" fill="var(--teal-light)"/>
    </svg>
  </section>

  <address class="contact">
    Rua das Acácias nº214<br>
    São Paulo &nbsp;S.P.<br>
    11 4020-7315<br>
    11 4020-7316<br>
    www.trilhaviva.com.br
  </address>

</div>
</body>
</html>
```